Miriam Fenwick

I need a business card for my health consulting business specializing in yoga and coaching. I like clean, crisp designs. I would like some of the colors from the attachment to be incorporate. For font, I like Trajan Pro and Helvectica Neue but would be open to other similar fonts. The attached photo doesn't need to be incorporated directly but could be used as some sort of decoration. I would also like to have the icon incorporated into the design - but not the type.

Industry/Entity Type

Business

Font styles to use
Serif
Sans Serif

```html
<!DOCTYPE html>
<html lang="en">
<head>
<meta charset="utf-8">
<title>Miriam Fenwick Wellness – Business Card</title>
<link rel="stylesheet" href="https://fonts.googleapis.com/css2?family=Cinzel:wght@400;600&family=PT+Sans:wght@400;700&display=swap">
<style>
  :root {
    --stage: #000000;
    --card-light: #ffffff;
    --card-dark: #2f3033;
    --bronze: #a8784a;
    --sand: #ddd0c1;
    --ivory: #e8e0d4;
  }
  * { margin: 0; padding: 0; box-sizing: border-box; }
  html, body {
    width: 1200px; height: 900px; overflow: hidden;
    background: var(--stage);
  }
  .canvas { position: relative; width: 1200px; height: 900px; }
  .card {
    position: absolute; top: 271px;
    width: 457px; height: 281px; border-radius: 14px;
  }
  .card--front { left: 137px; background: var(--card-light); font-family: "PT Sans", Helvetica, Arial, sans-serif; color: var(--bronze); }
  .card--back { left: 626px; background: var(--card-dark); }

  .front-wordmark {
    position: absolute; left: 45px; top: 330px; 
  }
  .wordmark-light {
    position: absolute; left: 40px; top: 60px; width: 196px; height: 116px;
    display: flex; align-items: center; justify-content: center; text-align: center;
    font-family: "PT Sans", Helvetica, Arial, sans-serif; font-weight: 400;
    font-size: 19px; line-height: 1.25; color: var(--sand);
  }
  .contact { position: absolute; left: 262px; top: 96px; }
  .contact__name { font-size: 18px; font-weight: 700; line-height: 1; }
  .contact__line { font-size: 12.5px; line-height: 16px; }
  .contact__lines { margin-top: 17px; }
  .tagline {
    position: absolute; left: 0; right: 0; top: 217px; text-align: center;
    font-size: 16px;
  }

  .back-mark {
    position: absolute; left: 0; right: 0; top: 62px; text-align: center;
  }
  .back-mark__dot { display: block; margin: 0 auto 12px; }
  .wordmark-dark {
    font-family: "Cinzel", "Trajan Pro", Georgia, serif; font-weight: 400;
    font-size: 30px; line-height: 36px; letter-spacing: 2px;
    color: var(--ivory); text-transform: uppercase;
  }
  .website {
    position: absolute; left: 0; right: 0; top: 217px; text-align: center;
    font-family: "PT Sans", Helvetica, Arial, sans-serif;
    font-size: 14px; letter-spacing: 1.3px; color: var(--ivory);
  }
</style>
</head>
<body>
<main class="canvas">
  <section class="card card--front" aria-label="Card front">
    <div class="wordmark-light">Miriam Fenwick<br>Wellness</div>
    <div class="contact">
      <p class="contact__name">Miriam Fenwick</p>
      <div class="contact__lines">
        <p class="contact__line">miriam@miriamfenwick.com</p>
        <p class="contact__line">(555) 014-2286</p>
      </div>
    </div>
    <p class="tagline">Yoga Teacher, Health &amp; Wellness Coach</p>
  </section>

  <section class="card card--back" aria-label="Card back">
    <div class="back-mark">
      <svg class="back-mark__dot" width="22" height="22" viewBox="0 0 22 22" aria-hidden="true">
        <circle cx="11" cy="11" r="11" fill="#e8e0d4"/>
      </svg>
      <p class="wordmark-dark">Miriam Fenwick<br>Wellness</p>
    </div>
    <p class="website">www.miriamfenwick.com</p>
  </section>
</main>
</body>
</html>
```